Special release wine label

Marrow Creek Cellars is a small premium wine producer in the Barossa - South Australia. We are a five star rated winery, producing exceptional wines true to variety, region and house style. We have a very special parcel of wine that we wish to release as an exclusive wine. Visit www.marrowcreekcellars.com.au for further feel.

The wine will be called Marrow Creek Cellars, 2012, The Amber Reserve Shiraz - Cabernet.

The wine can be bottled in either a burgundy or Bordeaux shaped bottle

```html
<!DOCTYPE html>
<html lang="en">
<head>
<meta charset="utf-8">
<title>Marrow Creek Cellars – The Amber Reserve Shiraz - Cabernet 2012</title>
<link rel="stylesheet" href="https://fonts.googleapis.com/css2?family=Cinzel:wght@400&family=Cormorant+Garamond:wght@500&family=Great+Vibes&display=swap">
<style>
  :root {
    --page-bg: #ffffff;
    --wine-red: #8e1b22;
    --wine-red-dark: #5a0d12;
    --label-silver-light: #ffffff;
    --label-silver-mid: #eeeeee;
    --label-silver-deep: #d9d9d9;
    --ink: #2b2b2b;
    --rule: #9a9a9a;
    --engraving-light: #f2f2f2;
    --engraving-dark: #9c9c9c;
  }
  * { margin: 0; padding: 0; box-sizing: border-box; }
  html, body {
    width: 1200px;
    height: 1000px;
    overflow: hidden;
    background: var(--page-bg);
  }
  .canvas {
    position: relative;
    width: 1200px;
    height: 1000px;
  }

  /* Neck mark: winery name set as plain text */
  .neck-mark {
    position: absolute;
    left: 450px;
    top: 70px;
    width: 300px;
    text-align: center;
    font-family: "Cinzel", serif;
    font-weight: 400;
    color: var(--ink);
    font-size: 26px;
    letter-spacing: 0.14em;
    line-height: 1.5;
  }
  .neck-mark .mark-dot {
    display: block;
    width: 10px;
    height: 10px;
    margin: 0 auto 10px;
    border-radius: 50%;
    background: var(--wine-red);
  }

  /* Front label */
  .front-label {
    position: absolute;
    left: 400px;
    top: 235px;
    width: 400px;
    height: 715px;
  }
  .front-label .label-shape {
    position: absolute;
    inset: 0;
    width: 400px;
    height: 715px;
  }
  .vine-artwork {
    position: absolute;
    left: 40px;
    top: 45px;
    width: 320px;
    height: 315px;
    background: radial-gradient(ellipse at 50% 45%, var(--engraving-dark) 0%, #c4c4c4 38%, var(--engraving-light) 75%, rgba(255,255,255,0) 100%);
  }
  .label-rule {
    position: absolute;
    left: 40px;
    width: 320px;
    height: 1px;
    background: var(--rule);
  }
  .label-rule.upper { top: 422px; }
  .label-rule.lower { top: 484px; }
  .wine-name {
    position: absolute;
    left: 0;
    width: 400px;
    top: 434px;
    text-align: center;
    font-family: "Cinzel", serif;
    font-weight: 400;
    font-size: 27px;
    letter-spacing: 0.04em;
    color: var(--ink);
  }
  .varietal {
    position: absolute;
    left: 0;
    width: 400px;
    top: 500px;
    text-align: center;
    font-family: "Great Vibes", cursive;
    font-size: 38px;
    color: var(--wine-red);
  }
  .vintage {
    position: absolute;
    left: 0;
    width: 400px;
    top: 556px;
    text-align: center;
    font-family: "Cormorant Garamond", serif;
    font-weight: 500;
    font-size: 27px;
    color: var(--ink);
  }
  .volume {
    position: absolute;
    left: 0;
    width: 400px;
    top: 654px;
    text-align: center;
    font-family: "Cormorant Garamond", serif;
    font-weight: 500;
    font-size: 22px;
    color: var(--ink);
  }
</style>
</head>
<body>
<main class="canvas">

  <div class="neck-mark">
    <span class="mark-dot"></span>
    Marrow Creek<br>Cellars
  </div>

  <section class="front-label">
    <svg class="label-shape" viewBox="0 0 400 715" aria-hidden="true">
      <defs>
        <linearGradient id="frameRed" x1="0" y1="0" x2="1" y2="1">
          <stop offset="0" stop-color="var(--wine-red)"/>
          <stop offset="0.5" stop-color="var(--wine-red-dark)"/>
          <stop offset="1" stop-color="var(--wine-red)"/>
        </linearGradient>
        <linearGradient id="labelSilver" x1="0" y1="0" x2="1" y2="1">
          <stop offset="0" stop-color="var(--label-silver-light)"/>
          <stop offset="0.45" stop-color="var(--label-silver-mid)"/>
          <stop offset="0.7" stop-color="var(--label-silver-light)"/>
          <stop offset="1" stop-color="var(--label-silver-deep)"/>
        </linearGradient>
      </defs>
      <path d="M0,45 Q200,-45 400,45 L400,715 L0,715 Z" fill="url(#frameRed)"/>
      <path d="M6,50 Q200,-33 394,50 L394,709 L6,709 Z" fill="url(#labelSilver)"/>
    </svg>

    <div class="vine-artwork" role="img" aria-label="Engraved illustration of a grape bunch with vine leaves and tendril on a fine-lined background"></div>

    <span class="label-rule upper"></span>
    <h1 class="wine-name">THE AMBER RESERVE</h1>
    <span class="label-rule lower"></span>
    <p class="varietal">Shiraz - Cabernet</p>
    <p class="vintage">2012</p>
    <p class="volume">750ML</p>
  </section>

</main>
</body>
</html>
```